依頼詳細
◆使用用途
サイト作成システム「モクリル」パンフレットなどの配布用の封筒

◆希望イメージ
「明るく、たのしく、ポップ」なイメージでお願いします!

◆デザインの要望
・原案をベースに、お渡しした材料をつかって作成してください。

・文言はそのまま使用してください。
・大きさの変更はOK
・文言の配置もデザインに合わせて移動OK

・「モクリル」ロゴは、別途制作するので、
簡易的なフォントで仮入れでお願いします。

あとは、デザイナー様の感性とセンスにすべておまかせします!

<<参考資料>>

素材(ドルネカロゴ、キャラ、企業ロゴ):
http://drk-q.com/img/publishing/20170329_dorunekalogo.zip

たくさんの方から応募、お待ちしております♪
どうぞ、よろしくお願いいたします!

記載項目
添付データを参照してください。
希望イメージ
• +5 0 +5
• シンプル
複雑
• 単色
カラフル
• 暗い
明るい
• 日常
高級
• 遊び心
厳粛
• 未来的
伝統的
• 女性的
男性的
希望する色
納品ファイル
• イラストレーター形式 (.ai)
補足説明
◆添付データ
・封筒原案
・封筒テンプレート
・内容物の一例
依頼公開後の追記内容
依頼金額を30000円に変更して、延長しました。
依頼期間の延長、金額をアップさせていただきました。

理由としては、ご提案していただいたデザインが、似た感じになってしまったため、
もう少し別のイメージもいただければと思ったためです。

引き続きよろしくお願いいたします。
イメージカラーについて

素材フォルダの中に、
現在作成中のマニュアルの表紙デザインを入れております。

そのマニュアルの表紙は、「青」を基調としておりますが、
封筒のイメージカラーは、青に限定しているわけではありません。

依頼内容から、デザイナーさまの自由な発想で、
制作していただけますと幸いです。

よろしくお願いいたします。
たくさんのご提案ありがとうございました!

現在、1名の方に微調整をお願いしております。
そちらが完了しだい、当選とさせていただきます。

また機会がございましたら、よろしくお願いいたします。
■ 選んだ理由

イメージ通りのデザインのためです。

■ 提案者全員のお礼・コメント

この度は、沢山のご提案ありがとうございました!
今後も、このような案件がありましたら、依頼させていただきます。
お時間が合う際は、よろしくお願いいたします。

```html
<!DOCTYPE html>
<html lang="ja">
<head>
<meta charset="utf-8">
<title>モクリル 封筒</title>
<link href="https://fonts.googleapis.com/css2?family=M+PLUS+Rounded+1c:wght@500;700;800&display=swap" rel="stylesheet">
<style>
  :root {
    --paper: #ffffff;
    --backdrop: #f4f4f4;
    --edge: #8c8c8c;
    --lemon: #f0e92c;
    --lemon-soft: #f6f27a;
    --brand-blue: #1f86d6;
    --badge-blue: #2a9ee0;
    --alert-red: #e8322c;
    --ink: #3a3a3a;
    --leaf: #7fae2a;
    --leaf-dark: #5f8f1c;
  }
  * { margin: 0; padding: 0; box-sizing: border-box; }
  html, body { width: 833px; height: 1200px; overflow: hidden; background: var(--backdrop); }
  body { font-family: "M PLUS Rounded 1c", sans-serif; position: relative; }

  .envelope-outline { position: absolute; left: 0; top: 0; }

  .cover-panel {
    position: absolute; left: 92px; top: 84px; width: 658px; height: 822px;
    background: var(--lemon);
  }
  .address-window {
    position: absolute; left: 204px; top: 42px; width: 250px; height: 250px;
    border: 2px solid #d9cf1c; background: var(--lemon-soft);
  }
  .system-label {
    position: absolute; top: 344px; width: 100%; text-align: center;
    color: #fff; font-weight: 800; font-size: 27px; letter-spacing: 2px;
  }
  .product-name {
    position: absolute; top: 386px; left: 0; width: 100%; text-align: center;
    font-weight: 800; font-size: 104px; line-height: 1.1; color: var(--brand-blue);
    letter-spacing: 6px;
  }
  .maker-name {
    position: absolute; top: 470px; left: 520px;
    font-weight: 700; font-size: 17px; color: var(--brand-blue);
  }
  .manual-badge {
    position: absolute; left: 548px; top: 250px; width: 124px; height: 124px;
    border-radius: 50%; background: var(--badge-blue); color: #fff;
    display: flex; flex-direction: column; align-items: center; justify-content: center;
    text-align: center; font-weight: 700; font-size: 12px; line-height: 1.35;
  }
  .manual-badge .badge-name { font-size: 17px; font-weight: 800; color: #ffe93a; }
  .character-lineup {
    position: absolute; left: 0; top: 516px; width: 658px; height: 306px;
    background: linear-gradient(180deg, var(--lemon) 0%, #e9d86a 55%, #d6a66a 100%);
  }

  .headline {
    position: absolute; left: 0; top: 918px; width: 833px; text-align: center;
    font-weight: 800; color: var(--alert-red); font-size: 54px; letter-spacing: 1px;
  }
  .headline .soft { color: var(--ink); font-size: 40px; }
  .subline {
    position: absolute; left: 0; top: 996px; width: 833px; text-align: center;
    font-weight: 800; color: var(--ink); font-size: 35px;
  }
  .subline .accent { color: var(--alert-red); }

  .point-chip {
    position: absolute; top: 1070px; width: 78px; height: 78px; border-radius: 50%;
    background: var(--leaf); color: #fff; font-weight: 700; font-size: 14px;
    display: flex; align-items: center; justify-content: center; text-align: center; line-height: 1.3;
  }
  .point-chip.first { left: 120px; }
  .point-chip.second { left: 212px; }
  .invite {
    position: absolute; left: 310px; top: 1092px;
    font-weight: 700; font-size: 23px; color: var(--leaf-dark);
  }
  .cut-note {
    position: absolute; left: 660px; top: 1156px;
    font-size: 10px; font-weight: 500; color: var(--ink);
  }
</style>
</head>
<body>
  <svg class="envelope-outline" width="833" height="1200" viewBox="0 0 833 1200">
    <polygon points="56,78 97,14 745,14 786,78" fill="var(--paper)" stroke="var(--edge)" stroke-width="2"/>
    <rect x="56" y="78" width="730" height="1104" fill="var(--paper)" stroke="var(--edge)" stroke-width="2"/>
  </svg>

  <section class="cover-panel">
    <div class="address-window"></div>
    <p class="system-label">サイト作成システム</p>
    <h1 class="product-name">モクリル</h1>
    <p class="maker-name">by ドルネカ</p>
    <div class="manual-badge">
      <span>パソコン初心者</span>
      <span>も安心の</span>
      <span class="badge-name">モクリル</span>
      <span>マニュアル完全版</span>
      <span>同封</span>
    </div>
    <div class="character-lineup" role="img" aria-label="モクリルのキャラクター5体が並ぶイラスト"></div>
  </section>

  <p class="headline">テンプレートを選ぶだけ<span class="soft">で</span></p>
  <p class="subline">反応率の高い<span class="accent">サイト</span>がポンっと出来上がる</p>

  <div class="point-chip first">サイトの<br>知識不要</div>
  <div class="point-chip second">たったの<br>3ステップ</div>
  <p class="invite">あなただけのサイトを作ってみませんか?</p>
  <p class="cut-note">キリトリ線はこちら</p>
</body>
</html>
```